Finance Product Agency Business Card Design

We're an agency that provides products (service contracts, gap insurance, tire and wheel, etc) and support to dealership finance departments. We specialize in training finance producers to maximize their potential and also keep them up to date on the ever changing compliance and legal landscape. I'll attach an image of our logo, excited to see what you all come up with. Would also be interested in discussing our new website design with the winner.

Target Market(s)

auto dealerships

Industry/Entity Type

Business

Contact Information for Business Card

Dale Hoskirk
Phone 517.364.2908
Fax 877.245.3196
email Dale.Hoskirk@brightlanecoverage.com

Requirements
Must have
• basic contact information
Nice to have
• looking for something professional but modern

```html
<!DOCTYPE html>
<html lang="en">
<head>
<meta charset="utf-8">
<title>Brightlane Coverage – Business Card</title>
<link href="https://fonts.googleapis.com/css2?family=Open+Sans:wght@400;600;700&display=swap" rel="stylesheet">
<style>
  :root {
    --page-bg: #e9eaec;
    --card-top: #fbfbfb;
    --card-bottom: #eeeff0;
    --ink: #2f4a56;
    --ink-dark: #1c2a31;
    --band-top: #0f1417;
    --band-mid: #2c4451;
    --band-bottom: #3c5d6b;
    --band-text: #ffffff;
  }
  * { box-sizing: border-box; margin: 0; padding: 0; }
  html, body {
    width: 1200px;
    height: 900px;
    overflow: hidden;
    background: var(--page-bg);
    font-family: "Open Sans", Arial, sans-serif;
  }
  .stage {
    width: 1200px;
    height: 900px;
    display: flex;
    align-items: center;
    justify-content: center;
  }
  .business-card {
    position: relative;
    width: 846px;
    height: 520px;
    border-radius: 22px;
    overflow: hidden;
    background: linear-gradient(180deg, var(--card-top), var(--card-bottom));
    box-shadow: 0 10px 30px rgba(0,0,0,0.15);
  }
  .holder-name {
    position: absolute;
    top: 46px;
    left: 0;
    width: 560px;
    text-align: center;
    font-weight: 700;
    font-size: 29px;
    letter-spacing: 1px;
    color: var(--ink);
  }
  .brand {
    position: absolute;
    top: 150px;
    left: 165px;
    display: flex;
    align-items: center;
    gap: 22px;
  }
  .brand-dot {
    width: 96px;
    height: 96px;
    border-radius: 50%;
    background: var(--ink);
    flex: none;
  }
  .brand-name {
    font-weight: 700;
    font-size: 52px;
    line-height: 1.05;
    letter-spacing: 1px;
    color: var(--ink-dark);
    text-transform: uppercase;
  }
  .contact-lines {
    position: absolute;
    top: 328px;
    left: 340px;
    display: flex;
    flex-direction: column;
    gap: 8px;
    font-size: 22px;
    color: var(--ink-dark);
  }
  .contact-line { display: flex; align-items: center; gap: 10px; }
  .contact-line svg { width: 17px; height: 17px; fill: var(--ink); }
  .email-band {
    position: absolute;
    left: 0;
    bottom: 0;
    width: 100%;
    height: 96px;
    background: linear-gradient(180deg, var(--band-top) 0%, var(--band-mid) 45%, var(--band-bottom) 100%);
    display: flex;
    align-items: center;
    justify-content: center;
    gap: 10px;
    color: var(--band-text);
    font-size: 22px;
    padding-top: 8px;
  }
  .email-band svg { width: 18px; height: 14px; fill: var(--band-text); }
</style>
</head>
<body>
<main class="stage">
  <section class="business-card">
    <h1 class="holder-name">DALE HOSKIRK</h1>

    <div class="brand">
      <span class="brand-dot"></span>
      <span class="brand-name">Brightlane<br>Coverage</span>
    </div>

    <div class="contact-lines">
      <div class="contact-line">
        <svg viewBox="0 0 24 24" aria-hidden="true"><path d="M6.6 10.8c1.4 2.8 3.8 5.1 6.6 6.6l2.2-2.2c.3-.3.7-.4 1-.2 1.1.4 2.3.6 3.6.6.6 0 1 .4 1 1V20c0 .6-.4 1-1 1C10.6 21 3 13.4 3 4c0-.6.4-1 1-1h3.5c.6 0 1 .4 1 1 0 1.3.2 2.5.6 3.6.1.3 0 .7-.2 1z"/></svg>
        <span>517.364.2908</span>
      </div>
      <div class="contact-line">
        <svg viewBox="0 0 24 24" aria-hidden="true"><path d="M7 2h9v5H7z M3 8h18v12H3z M5 10v8h3v-8z M11 11h2v2h-2zm4 0h2v2h-2zm-4 4h2v2h-2zm4 0h2v2h-2z"/></svg>
        <span>877.245.3196</span>
      </div>
    </div>

    <div class="email-band">
      <svg viewBox="0 0 18 14" aria-hidden="true"><path d="M0 0h18v14H0z M1.5 1.5 9 7.5l7.5-6z" fill-rule="evenodd"/></svg>
      <span>Dale.Hoskirk@brightlanecoverage.com</span>
    </div>
  </section>
</main>
</body>
</html>
```